Flyer Design for Private Car Service

Flyer should cater to Business Travelers and Executives who travel Business Class or First Class.
Flyer should include images attached.
Flyer should include the below text
Dallas to Austin
Chauffeured SUVs
• Travel Dallas to Austin in a new 2025 Marlow Strider for $499 one-way
• Trip includes a Uniformed Chauffeur who has a Commercial Drivers License (CDL)
• You can Schedule Chauffeur Pickup at Your Home in Dallas
• Our Chauffeur will Drop You Off at Your Final Destination in Austin
• You can Schedule Chauffeur Return Pickup in Austin and Return Back to Dallas.
• We offer Faster Times on Door-to-Door Travel than Bluecrest Airways
• We offer Comparable Prices on Door-to-Door Travel Times than Bluecrest Airways
• All of our trips are insured with $500k of commercial auto insurance
• Our Passengers can Talk on Cell Phone & Conduct Quill calls Throughout Travel
• Our Passengers have Maximum Privacy, Comfort and First-Class Amenities.
• Our Passengers Avoid Harwick Vale Field and KPR Airport hassles & delays
• Member Brenton Chamber of Commerce, Larkmoor Chamber of Commerce.
• Book your trip today at www.ridemarquel.example
Target Market(s)
Business Travelers
Look and feel
Each slider illustrates characteristics of the customer's brand and the style your logo design should communicate.

```html
<!DOCTYPE html>
<html lang="en">
<head>
<meta charset="utf-8">
<title>Dallas to Austin Chauffeured SUVs – Flyer</title>
<link rel="stylesheet" href="https://fonts.googleapis.com/css2?family=Montserrat:wght@500;600;700;800&family=Poppins:wght@400;600;700&display=swap">
<style>
  :root {
    --red: #e8141b;
    --red-dark: #b80d12;
    --ink: #141414;
    --white: #ffffff;
    --stage: #c6c6c6;
    --pill-grey: #e4e4e4;
  }
  * { box-sizing: border-box; margin: 0; padding: 0; }
  html, body { width: 1200px; height: 1200px; overflow: hidden; }
  body { background: var(--stage); position: relative; font-family: "Poppins", sans-serif; }

  .flyer {
    position: absolute; left: 178px; top: 20px;
    width: 844px; height: 1160px;
    background: var(--white); overflow: hidden;
  }
  .flyer-art { position: absolute; inset: 0; }

  .brand {
    position: absolute; left: 236px; top: 116px;
    transform: translateX(-50%);
    white-space: nowrap;
    font-family: "Montserrat", sans-serif; font-weight: 500;
    font-size: 28px; line-height: 34px; letter-spacing: 3px; color: var(--white);
  }

  .headline {
    position: absolute; left: 81px; top: 172px;
    font-family: "Montserrat", sans-serif; font-weight: 800;
    font-size: 66px; line-height: 58px; color: var(--white);
    letter-spacing: -0.5px;
  }
  .headline .accent { color: var(--red); }

  .offer-line {
    position: absolute; left: 0; width: 844px; top: 617px; text-align: center;
    font-family: "Montserrat", sans-serif; font-weight: 600;
    font-size: 25px; color: var(--white);
  }
  .price-pill {
    position: absolute; left: 218px; top: 655px; width: 411px; height: 48px;
    border-radius: 24px;
    background: linear-gradient(180deg, #ff2a2a 0%, var(--red) 55%, var(--red-dark) 100%);
    color: var(--white); text-align: center;
    font-family: "Montserrat", sans-serif; font-weight: 800;
    font-size: 29px; line-height: 48px;
  }

  .features {
    position: absolute; top: 804px; list-style: none;
    font-size: 14px; line-height: 20.5px; color: var(--ink);
  }
  .features.left { left: 53px; width: 360px; }
  .features.right { left: 457px; width: 345px; }
  .features li { position: relative; padding-left: 22px; }
  .features strong { font-weight: 700; }
  .features .tick { position: absolute; left: 0; top: 3px; width: 13px; height: 13px; }

  .contact-label {
    position: absolute; right: 66px; top: 1010px;
    font-weight: 700; font-size: 17px; color: var(--ink);
  }
  .phone-pill {
    position: absolute; left: 450px; top: 1039px; width: 338px; height: 60px;
    border-radius: 30px; background: var(--pill-grey);
  }
  .phone-pill .phone-icon { position: absolute; left: 6px; top: 6px; width: 48px; height: 48px; }
  .phone-pill .phone-number {
    position: absolute; left: 68px; top: 0; line-height: 60px;
    font-weight: 700; font-size: 35px; color: var(--ink); letter-spacing: 1px;
  }

  .rule { position: absolute; left: 0; top: 1067px; width: 448px; height: 4px; background: var(--red); }

  .book-tab { position: absolute; left: 0; top: 1088px; width: 444px; height: 72px; }
  .book-tab .book-text {
    position: absolute; left: 55px; top: 0; line-height: 72px;
    font-weight: 700; font-size: 28px; color: var(--white);
  }
  .web {
    position: absolute; left: 461px; top: 1108px;
    display: flex; align-items: center; gap: 9px;
    font-weight: 700; font-size: 23px; color: var(--ink);
  }
  .web svg { width: 22px; height: 22px; }
</style>
</head>
<body>
<main class="flyer">
  <svg class="flyer-art" viewBox="0 0 844 1160" width="844" height="1160">
    <defs>
      <linearGradient id="heroTone" x1="0" y1="0" x2="1" y2="1">
        <stop offset="0" stop-color="#6b6b6b"/>
        <stop offset="0.45" stop-color="#2b2b2b"/>
        <stop offset="1" stop-color="#3a3330"/>
      </linearGradient>
      <linearGradient id="bandTone" x1="0" y1="0" x2="1" y2="0">
        <stop offset="0" stop-color="#8fb3cf"/>
        <stop offset="0.3" stop-color="#7d8f88"/>
        <stop offset="0.55" stop-color="#3a3a3a"/>
        <stop offset="1" stop-color="#1c1c1c"/>
      </linearGradient>
      <linearGradient id="swoosh" x1="0" y1="0" x2="1" y2="0">
        <stop offset="0" stop-color="#ff1e1e"/>
        <stop offset="1" stop-color="#c40c12"/>
      </linearGradient>
    </defs>

    <path role="img" aria-label="Photo: Dallas skyline with arch bridge and highway beside a line of uniformed chauffeurs"
          d="M0 360 H844 V773 Q560 700 0 800 Z" fill="url(#bandTone)"/>
    <rect x="0" y="611" width="844" height="110" fill="rgba(20,20,20,0.55)"/>

    <path d="M150 775 Q520 680 844 773 V815 Q620 720 150 775 Z" fill="url(#swoosh)"/>

    <path role="img" aria-label="Photo: uniformed chauffeur holding the door of a black SUV for a business executive"
          d="M0 0 H844 V383 Q540 505 0 383 Z" fill="url(#heroTone)"/>
    <path d="M0 383 Q540 505 844 383" fill="none" stroke="#ffffff" stroke-width="4"/>

    <path d="M0 1088 H423 L444 1160 H0 Z" fill="var(--red)"/>
  </svg>

  <div class="brand">MARQUEL RIDES</div>

  <h1 class="headline">DALLAS<br>TO AUSTIN<br><span class="accent">CHAUFFEURED</span><br>SUVS</h1>

  <p class="offer-line">Travel Dallas to Austin in a new 2025 Marlow Strider</p>
  <div class="price-pill">FOR $499 ONE-WAY</div>

  <ul class="features left">
    <li><svg class="tick" viewBox="0 0 14 14"><circle cx="7" cy="7" r="6" fill="none" stroke="#e8141b" stroke-width="1.4"/><path d="M4 7.2 6.2 9.3 10 5" fill="none" stroke="#e8141b" stroke-width="1.5"/></svg><strong>Trip includes</strong> a Uniformed Chauffeur who has a Commercial Drivers License (CDL)</li>
    <li><svg class="tick" viewBox="0 0 14 14"><circle cx="7" cy="7" r="6" fill="none" stroke="#e8141b" stroke-width="1.4"/><path d="M4 7.2 6.2 9.3 10 5" fill="none" stroke="#e8141b" stroke-width="1.5"/></svg><strong>You can Schedule</strong> Chauffeur Pickup at Your Home in Dallas</li>
    <li><svg class="tick" viewBox="0 0 14 14"><circle cx="7" cy="7" r="6" fill="none" stroke="#e8141b" stroke-width="1.4"/><path d="M4 7.2 6.2 9.3 10 5" fill="none" stroke="#e8141b" stroke-width="1.5"/></svg><strong>Our Chauffeur</strong> will Drop You Off at Your Final Destination in Austin</li>
    <li><svg class="tick" viewBox="0 0 14 14"><circle cx="7" cy="7" r="6" fill="none" stroke="#e8141b" stroke-width="1.4"/><path d="M4 7.2 6.2 9.3 10 5" fill="none" stroke="#e8141b" stroke-width="1.5"/></svg><strong>You can Schedule</strong> Chauffeur Return Pickup in Austin and Return Back to Dallas.</li>
    <li><svg class="tick" viewBox="0 0 14 14"><circle cx="7" cy="7" r="6" fill="none" stroke="#e8141b" stroke-width="1.4"/><path d="M4 7.2 6.2 9.3 10 5" fill="none" stroke="#e8141b" stroke-width="1.5"/></svg><strong>We offer</strong> Faster Times on Door-to-Door Travel than Bluecrest Airways</li>
    <li><svg class="tick" viewBox="0 0 14 14"><circle cx="7" cy="7" r="6" fill="none" stroke="#e8141b" stroke-width="1.4"/><path d="M4 7.2 6.2 9.3 10 5" fill="none" stroke="#e8141b" stroke-width="1.5"/></svg><strong>We offer</strong> Comparable Prices on Door-to-Door Travel Times than Bluecrest Airways</li>
  </ul>

  <ul class="features right">
    <li><svg class="tick" viewBox="0 0 14 14"><circle cx="7" cy="7" r="6" fill="none" stroke="#e8141b" stroke-width="1.4"/><path d="M4 7.2 6.2 9.3 10 5" fill="none" stroke="#e8141b" stroke-width="1.5"/></svg><strong>All of our trips</strong> are insured with $500k of commercial auto insurance</li>
    <li><svg class="tick" viewBox="0 0 14 14"><circle cx="7" cy="7" r="6" fill="none" stroke="#e8141b" stroke-width="1.4"/><path d="M4 7.2 6.2 9.3 10 5" fill="none" stroke="#e8141b" stroke-width="1.5"/></svg><strong>Our Passengers</strong> can Talk on Cell Phone &amp; Conduct Quill calls Throughout Travel</li>
    <li><svg class="tick" viewBox="0 0 14 14"><circle cx="7" cy="7" r="6" fill="none" stroke="#e8141b" stroke-width="1.4"/><path d="M4 7.2 6.2 9.3 10 5" fill="none" stroke="#e8141b" stroke-width="1.5"/></svg><strong>Our Passengers</strong> have Maximum Privacy, Comfort and First-Class Amenities.</li>
    <li><svg class="tick" viewBox="0 0 14 14"><circle cx="7" cy="7" r="6" fill="none" stroke="#e8141b" stroke-width="1.4"/><path d="M4 7.2 6.2 9.3 10 5" fill="none" stroke="#e8141b" stroke-width="1.5"/></svg><strong>Our Passengers</strong> Avoid Harwick Vale Field and KPR Airport hassles &amp; delays</li>
    <li><svg class="tick" viewBox="0 0 14 14"><circle cx="7" cy="7" r="6" fill="none" stroke="#e8141b" stroke-width="1.4"/><path d="M4 7.2 6.2 9.3 10 5" fill="none" stroke="#e8141b" stroke-width="1.5"/></svg><strong>Member</strong> Brenton Chamber of Commerce, Larkmoor Chamber of Commerce.</li>
  </ul>

  <div class="contact-label">Contact us</div>
  <div class="phone-pill">
    <svg class="phone-icon" viewBox="0 0 48 48">
      <circle cx="24" cy="24" r="24" fill="#e8141b"/>
      <path d="M17 14c1-1 2.5-1 3.3 0l2.4 3.2c.7 1 .6 2.2-.2 3l-1.5 1.5c1.2 2.6 3.3 4.7 5.900 5.9l1.5-1.5c.8-.8 2-.9 3-.2l3.2 2.4c1 .8 1 2.3 0 3.3l-1.6 1.6c-1.3 1.3-3.3 1.7-5 .9C21.8 31.8 16.2 26.2 14.1 20c-.7-1.7-.3-3.7.9-5z" fill="#ffffff"/>
      <path d="M27 15a7 7 0 0 1 6 6M27 11a11 11 0 0 1 10 10" fill="none" stroke="#ffffff" stroke-width="1.8" stroke-linecap="round"/>
    </svg>
    <span class="phone-number">555-014-2290</span>
  </div>

  <div class="rule"></div>

  <div class="book-tab"><span class="book-text">Book your trip today at</span></div>
  <div class="web">
    <svg viewBox="0 0 24 24"><circle cx="12" cy="12" r="10" fill="none" stroke="#141414" stroke-width="1.8"/><ellipse cx="12" cy="12" rx="4.5" ry="10" fill="none" stroke="#141414" stroke-width="1.6"/><path d="M2 12h20M4 7h16M4 17h16" stroke="#141414" stroke-width="1.4"/></svg>
    <span>www.ridemarquel.example</span>
  </div>
</main>
</body>
</html>
```